Innovative psychologist for companies seeks web design for website

Psychologist offers 2 topics:
1. What can a company do to ensure that employees are satisfied and enjoy their work?
The following explanatory video is linked on the website:
https://www.vidplumora.com/watch?v=qTr8ZpLmW3d
2. How can you successfully change your own behavior?
Explanatory video: https://www.vidplumora.com/watch?v=HxK2vQeRt7b&t=6s
The slogan for the second theme will be: YOU are the pirate of your life!

Target Market(s)

companies and private individuals

Number of Pages Required

1 page

Requirements
Nice to have
• Characteristics of the psychologist: pragmatic, down-to-earth, honest, direct, appreciative, enjoys life, loves nature

```html
<!DOCTYPE html>
<html lang="en">
<head>
<meta charset="utf-8">
<title>Lukas Brenner – Psychologist</title>
<link rel="stylesheet" href="https://fonts.googleapis.com/css2?family=Poppins:wght@400;500;600;700&family=Cinzel:wght@500&display=swap">
<style>
:root{
  --blue:#1f73db;
  --ink:#3a3a3a;
  --text:#2b2b2b;
  --pale:#e9f1fa;
  --panel:#c6ddf3;
  --navy:#0b1c5a;
  --red:#d92639;
  --white:#ffffff;
}
*{margin:0;padding:0;box-sizing:border-box}
html,body{width:1200px;height:4184px;overflow:hidden}
body{position:relative;font-family:"Poppins",sans-serif;color:var(--text);background:var(--white)}
.abs{position:absolute}
a{color:inherit;text-decoration:none}

.hero{left:0;top:0;width:1200px;height:666px;background:linear-gradient(180deg,#b9d3ec 0%,#cfe0ef 45%,#6f9dc4 62%,#4f82b2 100%)}
.hero-person{left:0;top:150px;width:600px;height:516px;background:radial-gradient(ellipse at 55% 50%,rgba(240,238,236,.85),rgba(210,200,195,.35) 60%,transparent 75%)}
.nav{left:127px;top:37px;width:945px;height:82px;background:var(--white);border-radius:41px}
.logo{font-family:"Cinzel",serif;font-weight:500;font-size:25px;color:#222;letter-spacing:.5px}
.nav .logo{left:48px;top:23px}
.menu a{position:absolute;top:30px;font-size:15px;color:#222}
.menu .active::after{content:"";position:absolute;left:0;right:0;top:32px;height:3px;background:var(--blue)}
.slogan{left:643px;top:316px;font-size:53px;font-weight:600;line-height:62px;color:var(--white)}
.slogan u{text-decoration-thickness:3px;text-underline-offset:8px}

h2{font-size:39px;font-weight:600;color:var(--ink);line-height:48px}
.rule{height:4px;width:100px;background:var(--blue)}
.lead{font-size:20px;font-weight:500;line-height:28px;color:#222}
.body{font-size:15px;line-height:21px;color:#333}

.video{border:6px solid var(--blue);background:var(--white)}
.video .art{position:absolute;inset:20px;border-radius:4px}
.play{width:68px;height:68px}

.band{left:55px;top:1181px;width:1145px;height:518px;background:var(--pale)}

.portrait{left:560px;top:1803px;width:640px;height:568px;background:linear-gradient(135deg,#d9dcdc 0%,#c7c9c6 45%,#8f918c 100%)}
.signature{left:127px;top:2262px;width:340px;height:80px;background:linear-gradient(90deg,rgba(60,60,60,.08),rgba(60,60,60,.02));border-radius:6px}

.mind{left:0;top:2472px;width:565px;height:549px;background:radial-gradient(ellipse at 42% 50%,#1f4f7f 0%,#3b6a92 35%,#9fb3c6 70%,#c9d3dc 100%)}
.stripe{left:565px;top:2472px;width:33px;height:549px;background:var(--blue)}
.panel{left:598px;top:2472px;width:602px;height:549px;background:var(--panel)}
.traits li{position:absolute;list-style:none;font-size:19px;color:#222;display:flex;align-items:center;gap:8px}

.case{top:3289px;width:282px;height:357px}
.case span{position:absolute;left:30px;bottom:30px;right:20px;font-size:19px;font-weight:600;line-height:24px;color:var(--white)}

.footer{left:0;top:3784px;width:1200px;height:400px;background:linear-gradient(180deg,#0b1c5a 0%,#0a1a55 70%,#16327f 100%)}
.footer *{color:var(--white)}
.ftitle{font-size:18px;font-weight:600;letter-spacing:.3px}
.flinks a{position:absolute;font-size:14px}
.fcontact{font-size:14px;line-height:17px}
.ficon{width:38px;height:38px}
.social{width:22px;height:22px;border-radius:50%;border:2px solid var(--white)}
.copy{left:0;width:1200px;top:4133px;text-align:center;font-size:14px}
</style>
</head>
<body>

<section class="abs hero">
  <div class="abs hero-person" role="img" aria-label="Photo of a smiling woman with open arms by the sea"></div>
  <nav class="abs nav">
    <div class="abs logo">LUKAS BRENNER</div>
    <div class="menu">
      <a class="active" style="left:480px">Home</a>
      <a style="left:587px">About</a>
      <a style="left:693px">Services</a>
      <a style="left:818px">Contact</a>
    </div>
  </nav>
  <p class="abs slogan"><u>YOU</u> are the<br>pirate of your life!</p>
</section>

<section>
  <h2 class="abs" style="left:127px;top:780px">What Can Do</h2>
  <div class="abs rule" style="left:127px;top:836px"></div>
  <p class="abs lead" style="left:127px;top:856px;width:380px">What can a company do to ensure that employees are satisfied and enjoy their work?</p>
  <p class="abs body" style="left:127px;top:955px;width:380px">Lorem ipsum dolor sit amet, consectetur elit, sed do eiusmod tempor ilorncididunt ut labore et dol ore magna aliqua. Quis ipsum suspendisse uloltr ices gravida. Risus commodo viverra maecenas accumsan lacus vel facilisis.</p>
  <a class="abs video" href="https://www.vidplumora.com/watch?v=qTr8ZpLmW3d" style="left:591px;top:762px;width:482px;height:328px">
    <div class="art" role="img" aria-label="Cartoon of a puzzled manager beside a chart and tired employees in an office" style="background:linear-gradient(90deg,#f3f3f3 0%,#eef0f2 40%,#9cb3c7 55%,#c9a989 100%)"></div>
  </a>
  <svg class="abs play" style="left:560px;top:992px" viewBox="0 0 68 68" aria-hidden="true"><circle cx="34" cy="34" r="34" fill="#d92639"/><path d="M26 20 L50 34 L26 48Z" fill="#fff"/></svg>
</section>

<section>
  <div class="abs band"></div>
  <a class="abs video" href="https://www.vidplumora.com/watch?v=HxK2vQeRt7b&amp;t=6s" style="left:127px;top:1283px;width:480px;height:326px">
    <div class="art" role="img" aria-label="Cartoon of a man holding a trophy on a mountain, asking how to change behavior to reach goals" style="background:radial-gradient(circle at 50% 62%,#bfe3f0 0%,#9fd0e6 30%,#ffffff 55%)"></div>
  </a>
  <svg class="abs play" style="left:568px;top:1501px" viewBox="0 0 68 68" aria-hidden="true"><circle cx="34" cy="34" r="34" fill="#d92639"/><path d="M26 20 L50 34 L26 48Z" fill="#fff"/></svg>
  <h2 class="abs" style="left:700px;top:1313px">How Can Do</h2>
  <div class="abs rule" style="left:700px;top:1370px"></div>
  <p class="abs lead" style="left:702px;top:1389px;width:360px">How can you successfully change your own behavior?</p>
  <p class="abs body" style="left:702px;top:1460px;width:380px">Lorem ipsum dolor sit amet, consectetur elit, sed do eiusmod tempor ilorncididunt ut labore et dol ore magna aliqua. Quis ipsum suspendisse ulotr ices gravida. Risus commodo viverra maecenas accumsan lacus vel facilisis.</p>
</section>

<section>
  <h2 class="abs" style="left:128px;top:1830px">About<br>Lukas Brenner</h2>
  <div class="abs rule" style="left:128px;top:1936px"></div>
  <p class="abs body" style="left:127px;top:1975px;width:390px">Sed ut perspiciatis unde omnis iste natus error sit voluptatem accusantium doloremque laudantium, totam rem aperiam, eaque ipsa quae ab illo inve ntore veritatis et quasi architecto beatae vitae dic ta sunt explicabo. Nemo enim ipsam voluptatem quia voluptas sit aspernatur aut odit aut fugit, sed quia consequuntur magni dolores eos qui ratione voluptatem sequi nesciunt. Neque porro quisquam est, qui dolorem ipsum quia dolor sit ame conse ctetur, adipisci velit, sed quia non numquam eius modi tempora incidunt ut labor.</p>
  <div class="abs signature" role="img" aria-label="Handwritten signature of Lukas Brenner"></div>
  <div class="abs portrait" role="img" aria-label="Photo of the psychologist in glasses seated on a sofa holding a notepad"></div>
</section>

<section>
  <div class="abs mind" role="img" aria-label="Head silhouette filled with a glowing brain against a cloudy sky"></div>
  <div class="abs stripe"></div>
  <div class="abs panel"></div>
  <h2 class="abs" style="left:664px;top:2536px">Characteristics<br>of the psychologist:</h2>
  <div class="abs rule" style="left:664px;top:2642px"></div>
  <p class="abs body" style="left:662px;top:2672px;width:420px">Sed ut perspiciatis unde omnis iste natus error sit yloc us antium doloremque laudantium ut perspiciis unde omnis iste natus eroloremque laudantium totam.</p>
  <ul class="traits">
    <li style="left:662px;top:2776px"><svg width="18" height="18" viewBox="0 0 18 18"><circle cx="9" cy="9" r="7.5" fill="none" stroke="#1f73db" stroke-width="1.6"/><path d="M5.5 9.2l2.3 2.3 4.6-4.8" fill="none" stroke="#1f73db" stroke-width="1.6"/></svg>Pragmatic</li>
    <li style="left:662px;top:2821px"><svg width="18" height="18" viewBox="0 0 18 18"><circle cx="9" cy="9" r="7.5" fill="none" stroke="#1f73db" stroke-width="1.6"/><path d="M5.5 9.2l2.3 2.3 4.6-4.8" fill="none" stroke="#1f73db" stroke-width="1.6"/></svg>Down-to-earth</li>
    <li style="left:662px;top:2866px"><svg width="18" height="18" viewBox="0 0 18 18"><circle cx="9" cy="9" r="7.5" fill="none" stroke="#1f73db" stroke-width="1.6"/><path d="M5.5 9.2l2.3 2.3 4.6-4.8" fill="none" stroke="#1f73db" stroke-width="1.6"/></svg>Honest</li>
    <li style="left:662px;top:2911px"><svg width="18" height="18" viewBox="0 0 18 18"><circle cx="9" cy="9" r="7.5" fill="none" stroke="#1f73db" stroke-width="1.6"/><path d="M5.5 9.2l2.3 2.3 4.6-4.8" fill="none" stroke="#1f73db" stroke-width="1.6"/></svg>Direct</li>
    <li style="left:898px;top:2776px"><svg width="18" height="18" viewBox="0 0 18 18"><circle cx="9" cy="9" r="7.5" fill="none" stroke="#1f73db" stroke-width="1.6"/><path d="M5.5 9.2l2.3 2.3 4.6-4.8" fill="none" stroke="#1f73db" stroke-width="1.6"/></svg>Appreciative</li>
    <li style="left:898px;top:2821px"><svg width="18" height="18" viewBox="0 0 18 18"><circle cx="9" cy="9" r="7.5" fill="none" stroke="#1f73db" stroke-width="1.6"/><path d="M5.5 9.2l2.3 2.3 4.6-4.8" fill="none" stroke="#1f73db" stroke-width="1.6"/></svg>Enjoys life</li>
    <li style="left:898px;top:2866px"><svg width="18" height="18" viewBox="0 0 18 18"><circle cx="9" cy="9" r="7.5" fill="none" stroke="#1f73db" stroke-width="1.6"/><path d="M5.5 9.2l2.3 2.3 4.6-4.8" fill="none" stroke="#1f73db" stroke-width="1.6"/></svg>Loves nature</li>
  </ul>
</section>

<section>
  <h2 class="abs" style="left:0;width:1200px;top:3183px;text-align:center">Case Studies</h2>
  <div class="abs rule" style="left:550px;top:3244px"></div>
  <div class="abs case" style="left:127px;background:linear-gradient(180deg,#4b5d86 0%,#a35b7c 25%,#3c3f4e 60%,#1f1f22 100%)" role="img" aria-label="Profile of a face with a digital network overlay">
    <span>Lorem ipsum dolor sit amet, consectetur.</span></div>
  <div class="abs case" style="left:458px;background:linear-gradient(180deg,#3a6fa4 0%,#5d88b4 45%,#2f6ed6 75%,#1f63e0 100%)" role="img" aria-label="Clasped hands in a consultation">
    <span>Lorem ipsum dolor sit amet, consectetur.</span></div>
  <div class="abs case" style="left:789px;background:linear-gradient(180deg,#e2dfd8 0%,#c9c2b5 45%,#5a5853 78%,#262626 100%)" role="img" aria-label="Therapist taking notes on a notepad">
    <span>Lorem ipsum dolor sit amet, consectetur.</span></div>
</section>

<footer class="abs footer">
  <div class="abs logo" style="left:127px;top:70px;font-size:22px">LUKAS BRENNER</div>
  <p class="abs" style="left:125px;top:125px;width:265px;font-size:14px;line-height:20px">Lorem ipsum dolor sit amet, consec tetur adipiscing elit, sed eiusmod tempor incididunt ut labore loriose dolore magna aliqua loreipsum suspendisse ultrices gravida.</p>
  <div class="abs social" style="left:130px;top:239px" aria-label="Social profile"></div>
  <div class="abs social" style="left:171px;top:239px" aria-label="Social profile"></div>
  <div class="abs social" style="left:211px;top:239px" aria-label="Social profile"></div>

  <div class="abs ftitle" style="left:431px;top:58px">LINKS</div>
  <div class="flinks">
    <a style="left:434px;top:116px">Home</a>
    <a style="left:434px;top:149px">About</a>
    <a style="left:434px;top:182px">Services</a>
    <a style="left:434px;top:215px">How Can Do</a>
    <a style="left:434px;top:248px">Contact</a>
  </div>
  <div class="abs ftitle" style="left:607px;top:58px">SERVICES</div>
  <div class="flinks">
    <a style="left:607px;top:116px">Loisquam Service</a>
    <a style="left:607px;top:149px">Contrary to popular</a>
    <a style="left:607px;top:182px">Lorem Ipsummy</a>
    <a style="left:607px;top:215px">Loisquam Service</a>
    <a style="left:607px;top:248px">Contrary to plore</a>
  </div>
  <div class="abs ftitle" style="left:862px;top:58px">CONTACT</div>
  <svg class="abs ficon" style="left:862px;top:137px" viewBox="0 0 38 38"><circle cx="19" cy="19" r="18" fill="#1f73db" stroke="#fff" stroke-width="1.5"/><path d="M19 10a6 6 0 0 1 6 6c0 4.5-6 11-6 11s-6-6.5-6-11a6 6 0 0 1 6-6z" fill="#fff"/><circle cx="19" cy="16" r="2.2" fill="#1f73db"/></svg>
  <p class="abs fcontact" style="left:918px;top:140px">Lorem Dummyloac<br>Lor 345 Pind 338</p>
  <svg class="abs ficon" style="left:862px;top:195px" viewBox="0 0 38 38"><circle cx="19" cy="19" r="18" fill="#1f73db" stroke="#fff" stroke-width="1.5"/><path d="M14 11c1.5 0 2.5 3 2.5 4s-1.5 1.5-1 2.5c1 2 3 4 5 5 1 .5 1.5-1 2.5-1s4 1 4 2.5-2 3-3.5 3C17 27 11 21 11 14.5 11 13 12.5 11 14 11z" fill="#fff"/></svg>
  <p class="abs fcontact" style="left:918px;top:197px">Phone:<br>555 010 2284</p>
  <svg class="abs ficon" style="left:862px;top:257px" viewBox="0 0 38 38"><circle cx="19" cy="19" r="18" fill="#1f73db" stroke="#fff" stroke-width="1.5"/><rect x="11" y="13" width="16" height="12" rx="1.5" fill="#fff"/><path d="M11.5 14l7.5 6 7.5-6" fill="none" stroke="#1f73db" stroke-width="1.4"/></svg>
  <p class="abs fcontact" style="left:918px;top:259px">Email:<br>info@brennerpraxis.com</p>
</footer>
<p class="abs copy" style="color:#fff">Copyright © 2024 All rights are reserved.</p>

</body>
</html>
```